business card for real estate company

I need a sharp creative business card design that stands out for a real estate company that does the following
- Selling land
- Selling houses and apartments
- Property management

website www.velmoreestates.example
email: info at the above web address
phone number place holder

```html
<!DOCTYPE html>
<html lang="en">
<head>
<meta charset="utf-8">
<title>Velmore Estates – Business Card</title>
<link rel="stylesheet" href="https://fonts.googleapis.com/css2?family=Montserrat:wght@400;500;600;700&display=swap">
<style>
  :root {
    --navy: #14285a;
    --green: #6cbf3f;
    --white: #ffffff;
    --ink: #2b2f3a;
    --muted: #5d6475;
    --stage: #e6e8ec;
  }
  * { box-sizing: border-box; margin: 0; padding: 0; }
  html, body { width: 1200px; height: 900px; overflow: hidden; }
  body {
    background: var(--stage);
    font-family: "Montserrat", sans-serif;
    display: flex;
    align-items: center;
    justify-content: center;
    gap: 40px;
  }
  .card {
    position: relative;
    width: 540px;
    height: 310px;
    border-radius: 18px;
    background: var(--white);
    overflow: hidden;
    box-shadow: 0 6px 18px rgba(20, 40, 90, 0.18);
  }
  .card-ring {
    position: absolute;
    width: 96px; height: 96px;
    border: 5px solid var(--white);
    border-radius: 50%;
  }

  /* Front */
  .front-band {
    position: absolute; left: 0; right: 0; bottom: 0; height: 82px;
    background: var(--navy);
  }
  .front .card-ring { left: 120px; bottom: 34px; }
  .front-brand {
    position: absolute; left: 0; right: 0; top: 58px;
    text-align: center;
  }
  .brand-name {
    display: inline-flex; align-items: center; gap: 12px;
    font-weight: 700; color: var(--navy);
    font-size: 46px; letter-spacing: 2px; line-height: 1;
  }
  .brand-dot { width: 16px; height: 16px; border-radius: 50%; background: var(--green); }
  .brand-sub {
    display: block; margin-top: 8px;
    font-weight: 700; color: var(--navy);
    font-size: 20px; letter-spacing: 9px;
  }
  .tagline {
    display: block; margin-top: 8px;
    font-weight: 600; color: var(--green);
    font-size: 15px; letter-spacing: 0.5px;
  }
  .services {
    position: absolute; left: 22px; right: 22px; top: 200px;
    display: flex; justify-content: space-between;
    list-style: none;
  }
  .service {
    display: flex; align-items: center; gap: 7px;
    font-size: 13px; font-weight: 500; color: var(--ink);
  }
  .service svg { width: 16px; height: 16px; }

  /* Back */
  .back-panel {
    position: absolute; left: 0; top: 0; bottom: 0; width: 215px;
    background: var(--navy);
  }
  .back .card-ring { left: 166px; bottom: 26px; }
  .back-brand {
    position: absolute; left: 0; top: 46px; width: 215px;
    text-align: center; color: var(--white);
  }
  .back-brand .brand-name { color: var(--white); font-size: 28px; letter-spacing: 1.5px; gap: 8px; }
  .back-brand .brand-dot { width: 11px; height: 11px; }
  .back-brand .brand-sub { color: var(--white); font-size: 13px; letter-spacing: 6px; }

  .agent {
    position: absolute; right: 26px; top: 38px;
    display: flex; align-items: center; gap: 12px;
    text-align: right;
  }
  .agent-name { font-size: 21px; color: var(--navy); letter-spacing: 0.5px; }
  .agent-name strong { font-weight: 700; }
  .agent-name span { font-weight: 400; }
  .agent-role { font-size: 12px; color: var(--muted); margin-top: 2px; }
  .icon-box {
    width: 26px; height: 26px; border-radius: 3px;
    background: var(--navy);
    display: flex; align-items: center; justify-content: center;
    flex-shrink: 0;
  }
  .icon-box svg { width: 15px; height: 15px; }
  .contacts {
    position: absolute; right: 26px; top: 126px;
    list-style: none;
    display: flex; flex-direction: column; gap: 11px;
  }
  .contact {
    display: flex; align-items: center; justify-content: flex-end; gap: 12px;
    font-size: 12.5px; color: var(--ink);
  }
  .contact .icon-box { width: 22px; height: 22px; }
  .contact .icon-box svg { width: 13px; height: 13px; }
</style>
</head>
<body>

  <section class="card front" aria-label="Business card front">
    <div class="front-band"></div>
    <div class="card-ring"></div>
    <div class="front-brand">
      <span class="brand-name"><span class="brand-dot"></span>VELMORE</span>
      <span class="brand-sub">ESTATES</span>
      <span class="tagline">Integrity in Kenyan real estate</span>
    </div>
    <ul class="services">
      <li class="service">
        <svg viewBox="0 0 16 16" fill="none" stroke="#14285a" stroke-width="1.5"><path d="M2 8 8 2.5 14 8M4 7v6.5h8V7"/><rect x="6.5" y="9.5" width="3" height="4"/></svg>
        Selling houses &amp; apartments
      </li>
      <li class="service">
        <svg viewBox="0 0 16 16" fill="none" stroke="#14285a" stroke-width="1.5"><path d="M1.5 12.5 5 5l4 4 2-3 3.5 6.5z"/></svg>
        Selling land
      </li>
      <li class="service">
        <svg viewBox="0 0 16 16" fill="none" stroke="#14285a" stroke-width="1.5"><rect x="3" y="2" width="10" height="12"/><path d="M5.5 5h2M8.5 5h2M5.5 8h2M8.5 8h2M7 14v-3h2v3"/></svg>
        Property management
      </li>
    </ul>
  </section>

  <section class="card back" aria-label="Business card back">
    <div class="back-panel"></div>
    <div class="card-ring"></div>
    <div class="back-brand">
      <span class="brand-name"><span class="brand-dot"></span>VELMORE</span>
      <span class="brand-sub">ESTATES</span>
    </div>

    <div class="agent">
      <div>
        <div class="agent-name"><strong>JONAH</strong> <span>REED</span></div>
        <div class="agent-role">Real Estate Agent</div>
      </div>
      <div class="icon-box">
        <svg viewBox="0 0 16 16" fill="#fff"><circle cx="8" cy="5" r="3"/><path d="M2.5 15c0-3.5 2.5-5.5 5.5-5.5s5.5 2 5.5 5.5z"/></svg>
      </div>
    </div>

    <ul class="contacts">
      <li class="contact">+254 700 000 000
        <span class="icon-box"><svg viewBox="0 0 16 16" fill="#fff"><path d="M4 1.5 6.5 4 5 6c1 2 3 4 5 5l2-1.5 2.5 2.5-1.5 2.5C7.5 14 2 8.5 1.5 3z"/></svg></span>
      </li>
      <li class="contact">info@velmoreestates.example
        <span class="icon-box"><svg viewBox="0 0 16 16" fill="none" stroke="#fff" stroke-width="1.5"><rect x="1.5" y="3.5" width="13" height="9"/><path d="m1.5 3.5 6.5 5.5 6.5-5.5"/></svg></span>
      </li>
      <li class="contact">www.velmoreestates.example
        <span class="icon-box"><svg viewBox="0 0 16 16" fill="none" stroke="#fff" stroke-width="1.3"><circle cx="8" cy="8" r="6.5"/><ellipse cx="8" cy="8" rx="2.8" ry="6.5"/><path d="M1.5 8h13"/></svg></span>
      </li>
      <li class="contact">48 Harbor Lane, City name, Country
        <span class="icon-box"><svg viewBox="0 0 16 16" fill="#fff"><path d="M8 1a5 5 0 0 0-5 5c0 4 5 9 5 9s5-5 5-9a5 5 0 0 0-5-5zm0 7a2 2 0 1 1 0-4 2 2 0 0 1 0 4z"/></svg></span>
      </li>
    </ul>
  </section>

</body>
</html>
```